Tarrow Creek plumbing plumbing company business card design

Something sinilar to business card i upload it is my old business card design
And have a good watermark with the logo or majority of the logot in rhe background as watermark

Plumbing business similar to uploaded design with a nice watermark of the logo

Font styles to use
Script

Colors

Designer to choose colors to be used in the design.

```html
<!DOCTYPE html>
<html lang="en">
<head>
<meta charset="utf-8">
<title>Tarrow Creek Plumbing – Business Card</title>
<link rel="stylesheet" href="https://fonts.googleapis.com/css2?family=Lato:wght@400;700&family=Montserrat:wght@500;700&family=Great+Vibes&display=swap">
<style>
  :root {
    --backdrop: #7c7c7c;
    --card-white: #ffffff;
    --brand-blue: #0a78c2;
    --ink: #111111;
    --rule: #d9d9d9;
    --rule-dark: #8a8a8a;
    --night: #000000;
  }
  * { margin: 0; padding: 0; box-sizing: border-box; }
  html, body { width: 1200px; height: 1200px; overflow: hidden; }
  body { background: var(--backdrop); position: relative; font-family: "Lato", Arial, sans-serif; }

  .card { position: absolute; box-shadow: 2px 3px 6px rgba(0,0,0,.35); overflow: hidden; }

  .card-front { left: 234px; top: 310px; width: 364px; height: 594px; background: var(--card-white); text-align: center; color: var(--ink); }
  .brand-name { position: absolute; left: 0; right: 0; top: 158px; font-family: "Montserrat", Arial, sans-serif; font-weight: 700; font-size: 27px; line-height: 34px; letter-spacing: 2px; color: var(--ink); }
  .person-name { position: absolute; left: 0; right: 0; top: 348px; font-weight: 700; font-size: 24px; line-height: 28px; color: var(--brand-blue); }
  .person-role { position: absolute; left: 0; right: 0; top: 374px; font-family: "Great Vibes", cursive; font-size: 24px; line-height: 26px; }
  .icon-row { position: absolute; left: 87px; top: 411px; width: 190px; height: 26px; }
  .contact-list { position: absolute; left: 0; right: 0; top: 448px; font-size: 17px; line-height: 21.5px; list-style: none; }
  .contact-rule { position: absolute; left: 88px; width: 195px; top: 522px; height: 1px; background: var(--rule); }
  .licence { position: absolute; left: 0; right: 0; top: 537px; font-size: 17px; }
  .licence .label { color: var(--brand-blue); }

  .card-back { left: 627px; top: 310px; width: 369px; height: 595px; background: var(--night); }
  .back-band { position: absolute; left: 0; top: 0; width: 369px; height: 215px; background: var(--brand-blue); }
  .back-watermark { position: absolute; left: 20px; top: 60px; width: 380px; height: 380px; border-radius: 50%; background: var(--card-white); opacity: .14; }
  .back-name { position: absolute; left: 0; right: 0; top: 490px; text-align: center; color: var(--card-white); font-family: "Montserrat", Arial, sans-serif; font-weight: 500; font-size: 27px; letter-spacing: 6px; line-height: 39px; }
</style>
</head>
<body>
  <section class="card card-front">
    <div class="brand-name">TARROW CREEK<br>PLUMBING</div>
    <div class="person-name">MARCUS HALE</div>
    <div class="person-role">Managing Director</div>
    <svg class="icon-row" viewBox="0 0 190 26" aria-hidden="true">
      <line x1="0" y1="13" x2="54" y2="13" stroke="var(--rule-dark)" stroke-width="1"/>
      <line x1="136" y1="13" x2="190" y2="13" stroke="var(--rule-dark)" stroke-width="1"/>
      <circle cx="67" cy="13" r="12" fill="var(--brand-blue)"/>
      <path d="M61 10 q6 -5 12 0 l-2 2 h-2 l-1 -2 h-2 l-1 2 h-2z M62 13 h10 v4 h-10z" fill="#fff"/>
      <circle cx="95" cy="13" r="12" fill="var(--brand-blue)"/>
      <rect x="89" y="9" width="12" height="8" fill="#fff"/>
      <path d="M89 9 l6 5 l6 -5" fill="none" stroke="var(--brand-blue)" stroke-width="1.2"/>
      <circle cx="122" cy="13" r="12" fill="var(--brand-blue)"/>
      <circle cx="122" cy="13" r="6" fill="#fff"/>
      <path d="M119 10 q3 2 2 4 q3 1 4 4" fill="none" stroke="var(--brand-blue)" stroke-width="1.5"/>
    </svg>
    <ul class="contact-list">
      <li>044-987 654 321</li>
      <li>info@tarrowcreek.com</li>
      <li>www.tarrowcreek.com</li>
    </ul>
    <div class="contact-rule"></div>
    <div class="licence"><span class="label">LIC NO:</span> 458207c</div>
  </section>

  <section class="card card-back">
    <div class="back-band"></div>
    <div class="back-watermark" role="img" aria-label="Large faint company emblem watermark"></div>
    <div class="back-name">TARROW CREEK<br>PLUMBING</div>
  </section>
</body>
</html>
```